Business Card Design Project

Business Card design based on logo.

I need business card, letterhead, envelope, and if possible, Powerpoint slide template.

On front of business card: Just logo- and  my name and title:  Rosalind Pekar, Principal

On reverse-logo and the rest of the contact info:

4857 Orchard Lane
Davis, CA 95618
650-381-2276
rp@brindlestudyworks.example

On letterhead-Just logo at top, at bottom  the rest-very small along the bottom

On PPT slide-just the logo.

I also want to try a few other colors-I like lime/dark grey (not black) but would like to try Sienna, maybe also indigo or bright blue-green.

I forgot to add-

On the business card-switch to vertical on reverse side and put:

Reverse side-switch to vertical and list:

Rosalind Pekar
Principal
Brindle Study Works, LLC

650-381-2276

4857 Orchard Lane
Davis, CA 95618

Rosalind Pekar
Principal

650-381-2276

4857 Orchard Lane
Davis, CA 95618

I have another project at the same time-for Stationery. Feel free to submit to that one also.

That one includes letterhead, envelope, PPT slide, folder cover sheet-RP

Industry/Entity Type

Business

Requirements
Must have
• Must use logo-preferably lime green version-with gray, not black or just 2-tone -logo on colored background.

```html
<!DOCTYPE html>
<html lang="en">
<head>
<meta charset="utf-8">
<title>Brindle Study Works – Business Card</title>
<link rel="stylesheet" href="https://fonts.googleapis.com/css2?family=Open+Sans:wght@400;700&display=swap">
<style>
  :root {
    --backdrop: #2a2b2d;
    --card: #f6f6f5;
    --lime: #8dc21f;
    --ink: #4a4a4a;
    --ink-soft: #8a8a8a;
    --band: #2c2d2f;
    --band-edge: #3a3b3d;
    --rule: #e3e3e1;
  }
  * { box-sizing: border-box; margin: 0; padding: 0; }
  html, body {
    width: 1200px; height: 900px; overflow: hidden;
    background: var(--backdrop);
    font-family: "Open Sans", Arial, sans-serif;
  }
  .card {
    position: absolute; left: 180px; top: 210px;
    width: 840px; height: 480px;
    background: var(--card);
    box-shadow: 0 18px 40px rgba(0,0,0,.45);
    overflow: hidden;
  }
  .card__rule {
    position: absolute; left: 0; right: 0; top: 404px;
    height: 3px; background: var(--lime);
  }
  .card__band {
    position: absolute; left: 0; right: 0; top: 420px; bottom: 0;
    background: repeating-linear-gradient(135deg, var(--band) 0 3px, var(--band-edge) 3px 5px);
  }
  .card__divider {
    position: absolute; left: 432px; top: 60px; height: 300px;
    width: 1px; background: var(--rule);
  }
  .brand {
    position: absolute; left: 60px; top: 140px; width: 340px;
    display: flex; align-items: center; gap: 16px;
  }
  .brand__mark { width: 26px; height: 26px; background: var(--lime); flex: none; }
  .brand__name {
    color: var(--ink); font-weight: 700;
    font-size: 34px; line-height: 1.1; letter-spacing: 4px;
    text-transform: uppercase;
  }
  .person { position: absolute; left: 470px; top: 92px; }
  .person__name { color: var(--lime); font-weight: 700; font-size: 27px; line-height: 1.2; }
  .person__title { color: var(--ink-soft); font-size: 19px; line-height: 1.3; }
  .contact {
    position: absolute; left: 470px; top: 186px;
    list-style: none; color: var(--ink); font-size: 17px; line-height: 1.35;
  }
  .contact__item { display: flex; align-items: flex-start; gap: 14px; margin-bottom: 4px; }
  .contact__item--address { margin-bottom: 20px; }
  .contact__icon { width: 22px; height: 22px; flex: none; margin-top: 1px; }
</style>
</head>
<body>
  <article class="card">
    <div class="brand">
      <span class="brand__mark"></span>
      <span class="brand__name">Brindle<br>Study Works</span>
    </div>

    <div class="card__divider"></div>

    <header class="person">
      <p class="person__name">Rosalind Pekar</p>
      <p class="person__title">Principle</p>
    </header>

    <ul class="contact">
      <li class="contact__item contact__item--address">
        <svg class="contact__icon" viewBox="0 0 22 22" aria-hidden="true">
          <circle cx="11" cy="11" r="11" fill="var(--lime)"/>
          <path d="M11 5a4 4 0 0 0-4 4c0 3 4 8 4 8s4-5 4-8a4 4 0 0 0-4-4z" fill="#fff"/>
          <circle cx="11" cy="9" r="1.5" fill="var(--lime)"/>
        </svg>
        <span>4857 Orchard Lane<br>Davis, CA 95618</span>
      </li>
      <li class="contact__item">
        <svg class="contact__icon" viewBox="0 0 22 22" aria-hidden="true">
          <circle cx="11" cy="11" r="11" fill="var(--lime)"/>
          <path d="M7 6h2.5l1 3-1.5 1a7 7 0 0 0 3 3l1-1.5 3 1V15a1.5 1.5 0 0 1-1.5 1.5A9 9 0 0 1 5.5 7.5 1.5 1.5 0 0 1 7 6z" fill="#fff"/>
        </svg>
        <span>650-381-2276</span>
      </li>
      <li class="contact__item">
        <svg class="contact__icon" viewBox="0 0 22 22" aria-hidden="true">
          <circle cx="11" cy="11" r="11" fill="var(--lime)"/>
          <rect x="6" y="9" width="10" height="7" rx="1" fill="#fff"/>
          <rect x="8" y="5.5" width="6" height="4" fill="#fff"/>
        </svg>
        <span>650-381-2277</span>
      </li>
      <li class="contact__item">
        <svg class="contact__icon" viewBox="0 0 22 22" aria-hidden="true">
          <circle cx="11" cy="11" r="11" fill="var(--lime)"/>
          <rect x="5.5" y="7" width="11" height="8" rx="1" fill="#fff"/>
          <path d="M5.5 7.5 11 11.5l5.5-4" stroke="var(--lime)" stroke-width="1.2" fill="none"/>
        </svg>
        <span>rp@brindlestudyworks.example</span>
      </li>
      <li class="contact__item">
        <svg class="contact__icon" viewBox="0 0 22 22" aria-hidden="true">
          <circle cx="11" cy="11" r="11" fill="var(--lime)"/>
          <circle cx="11" cy="11" r="5.5" stroke="#fff" stroke-width="1.3" fill="none"/>
          <path d="M5.5 11h11M11 5.5c-2.5 3-2.5 8 0 11M11 5.5c2.5 3 2.5 8 0 11" stroke="#fff" stroke-width="1.1" fill="none"/>
        </svg>
        <span>www.brindlestudyworks.example</span>
      </li>
    </ul>

    <div class="card__rule"></div>
    <div class="card__band"></div>
  </article>
</body>
</html>
```